Talbix Pens needs a new Webpage for their collection of ballpens

We at Talbix pens need a brand new webpage to represent our company and range of products. We need a product based website to focus purely on our collection. The web design must bring about a perception of high quality International brand but still affordable in price. Since there are only 5 products, they must all feature on the cover page itself.

Target Market(s)

Stationary Wholesale and retail

Industry/Entity Type

It Company

Number of Pages Required

1 page

Requirements
Must have
• pls see www.quendora-example.com to derive inspiration
Should not have
• stock images
• abstract images
• random pen images

```html
<!DOCTYPE html>
<html lang="en">
<head>
<meta charset="utf-8">
<title>Talbix Pens</title>
<link rel="stylesheet" href="https://fonts.googleapis.com/css2?family=Open+Sans:wght@300;400;700&family=Oswald:wght@200&display=swap">
<style>
  :root {
    --page: #f0f0f0;
    --brand: #1f66a3;
    --brand-band: #2c74aa;
    --footer-band: #1a64a0;
    --ink: #333333;
    --muted: #8a8a8a;
    --white: #ffffff;
    --bar: #111111;
    --pen-violet: #3b2a9a;
    --pen-clear: #dfe3ea;
    --pen-sky: #8cbfe8;
    --swatch-blue: #0a2f9e;
    --swatch-black: #000000;
    --swatch-red: #ff1a1a;
  }
  * { box-sizing: border-box; margin: 0; padding: 0; }
  html, body { width: 678px; height: 1200px; overflow: hidden; }
  body {
    position: relative;
    background: var(--page);
    font-family: "Open Sans", Arial, sans-serif;
    color: var(--ink);
  }
  .top-rule { position: absolute; left: 0; top: 0; width: 678px; height: 3px; background: var(--brand); }

  .site-header { position: absolute; left: 0; top: 0; width: 678px; height: 70px; }
  .brand-name {
    position: absolute; left: 44px; top: 16px;
    font-size: 27px; font-weight: 400; letter-spacing: 3px; color: var(--brand);
  }
  .main-nav { position: absolute; right: 45px; top: 28px; display: flex; gap: 27px; }
  .main-nav a { font-size: 10.5px; color: var(--ink); text-decoration: none; }
  .main-nav a.is-active { color: var(--brand); }

  .hero-pen {
    position: absolute; left: 44px; top: 134px; width: 590px; height: 38px;
    border-radius: 6px 19px 19px 6px;
    background: linear-gradient(90deg, var(--pen-violet) 0 7%, var(--pen-clear) 7% 67%, var(--pen-violet) 67% 100%);
  }
  .hero-title {
    position: absolute; left: 0; top: 223px; width: 678px; text-align: center;
    font-size: 24px; font-weight: 300; color: var(--brand);
  }
  .slider-dots { position: absolute; left: 0; top: 290px; width: 678px; display: flex; justify-content: center; gap: 8px; }
  .slider-dots span { width: 10px; height: 10px; border-radius: 50%; border: 1px solid var(--brand); }
  .slider-dots span.is-current { background: var(--brand); }

  .wave { position: absolute; left: 0; width: 678px; display: block; }

  .about-band { position: absolute; left: 0; top: 338px; width: 678px; height: 310px; background: var(--brand-band); }
  .about-title {
    position: absolute; left: 44px; top: 362px;
    font-size: 37px; font-weight: 300; color: var(--white);
  }
  .about-copy { position: absolute; left: 45px; top: 415px; width: 310px; color: var(--white); font-size: 8.8px; line-height: 14px; }
  .about-copy p + p { margin-top: 14px; }
  .promise-ring {
    position: absolute; left: 395px; top: 366px; width: 234px; height: 234px;
    border: 1px solid var(--white); border-radius: 50%;
  }
  .promise-lead {
    position: absolute; left: 395px; top: 434px; width: 234px; text-align: center;
    font-family: "Oswald", "Arial Narrow", sans-serif; font-weight: 200; font-size: 25px; color: var(--white);
  }
  .promise-strong {
    position: absolute; left: 395px; top: 476px; width: 234px; text-align: center;
    font-size: 21px; font-weight: 700; color: var(--white);
  }
  .promise-rule { position: absolute; left: 443px; top: 518px; width: 142px; height: 1px; background: var(--white); }
  .promise-pen {
    position: absolute; left: 423px; top: 533px; width: 182px; height: 9px; border-radius: 3px 5px 5px 3px;
    background: linear-gradient(90deg, var(--pen-violet) 0 6%, var(--pen-clear) 6% 67%, var(--pen-violet) 67% 100%);
  }

  .products-title {
    position: absolute; left: 0; top: 672px; width: 678px; text-align: center;
    font-size: 36px; font-weight: 400; color: var(--brand);
  }
  .product { position: absolute; top: 724px; width: 200px; text-align: center; }
  .product-shot { margin: 0 auto; width: 120px; height: 148px; border-radius: 4px; }
  .shot-violet { background: linear-gradient(135deg, var(--page) 20%, #b9b2df 48%, var(--pen-violet) 52%, var(--page) 80%); }
  .shot-clear { background: linear-gradient(135deg, var(--page) 20%, var(--pen-clear) 45%, var(--pen-violet) 55%, var(--page) 80%); }
  .shot-sky { background: linear-gradient(135deg, var(--page) 20%, var(--pen-sky) 48%, #5c9fd6 52%, var(--page) 80%); }
  .product-name { margin-top: 12px; font-size: 15px; color: var(--brand); }
  .product-spec { margin-top: 3px; font-size: 10.5px; line-height: 18px; color: var(--muted); }
  .swatches { margin-top: 5px; display: flex; justify-content: center; gap: 9px; }
  .swatches span { width: 15px; height: 15px; }
  .sw-blue { background: var(--swatch-blue); }
  .sw-black { background: var(--swatch-black); }
  .sw-red { background: var(--swatch-red); }
  .carousel-arrows { position: absolute; left: 303px; top: 988px; display: flex; gap: 11px; }

  .footer-band { position: absolute; left: 0; top: 1056px; width: 678px; height: 114px; background: var(--footer-band); }
  .contact-list { position: absolute; left: 45px; top: 1098px; list-style: none; color: var(--white); font-size: 12px; }
  .contact-list li { display: flex; align-items: center; gap: 7px; height: 23px; }
  .contact-list .strong { font-weight: 700; }
  .social-links { position: absolute; left: 522px; top: 1114px; display: flex; gap: 11px; }
  .social-links span { width: 30px; height: 30px; border: 1px solid var(--white); border-radius: 50%; }
  .legal-bar {
    position: absolute; left: 0; top: 1170px; width: 678px; height: 30px; background: var(--bar);
    color: #d8d8d8; font-size: 9px; text-align: center; line-height: 30px;
  }
  .legal-bar strong { color: var(--white); }
</style>
</head>
<body>
  <div class="top-rule"></div>

  <header class="site-header">
    <div class="brand-name">TALBIX</div>
    <nav class="main-nav">
      <a class="is-active" href="#">HOME</a>
      <a href="#">ABOUT</a>
      <a href="#">PRODUCTS</a>
      <a href="#">CONTACT</a>
    </nav>
  </header>

  <section class="hero">
    <div class="hero-pen" role="img" aria-label="Talbix Orbit ballpen, violet cap and grip with clear barrel, shown horizontally"></div>
    <h1 class="hero-title">TALBIX ORBIT</h1>
    <div class="slider-dots"><span class="is-current"></span><span></span><span></span><span></span><span></span></div>
  </section>

  <section class="about">
    <div class="about-band"></div>
    <svg class="wave" style="top:328px" width="678" height="14" viewBox="0 0 678 14">
      <path d="M0 6 C120 2 220 10 340 7 S560 2 678 5 L678 14 L0 14 Z" fill="var(--brand-band)"/>
    </svg>
    <h2 class="about-title">ABOUT</h2>
    <div class="about-copy">
      <p>Lorem Ipsum is simply dummy text of the printing and typesetting industry. Lorem Ipsum has been the industry's standard dummy text ever since the 1500s, when an unknown printer took a galley of type and scrambled it to make a type specimen book. It has survived not only five centuries.</p>
      <p>but also the leap into electronic typesetting, remaining essentially unchanged. It was popularised in the 1960s with the release of Letraset sheets containing Lorem Ipsum passages, and more recently with desktop publishing software like Aldus PageMaker including versions of Lorem Ipsum.</p>
    </div>
    <div class="promise-ring"></div>
    <div class="promise-lead">INTERNATIONAL BRAND</div>
    <div class="promise-strong">AFFORDABLE PRICE</div>
    <div class="promise-rule"></div>
    <div class="promise-pen" role="img" aria-label="Small Talbix ballpen shown horizontally"></div>
    <svg class="wave" style="top:642px" width="678" height="12" viewBox="0 0 678 12">
      <path d="M0 2 C150 6 300 0 450 4 S600 6 678 3 L678 0 L0 0 Z" fill="var(--brand-band)"/>
      <path d="M0 6 C150 9 300 3 450 7 S600 9 678 6" fill="none" stroke="var(--brand-band)" stroke-width="0.8"/>
    </svg>
  </section>

  <section class="products">
    <h2 class="products-title">OUR PRODUCTS</h2>
    <article class="product" style="left:35px">
      <div class="product-shot shot-violet" role="img" aria-label="Talbix Lumen ballpen with violet barrel, shown diagonally"></div>
      <h3 class="product-name">Talbix Lumen</h3>
      <p class="product-spec">Tip size: 0.7mm<br>5pcs pouch</p>
      <div class="swatches"><span class="sw-blue"></span><span class="sw-black"></span><span class="sw-red"></span></div>
    </article>
    <article class="product" style="left:240px">
      <div class="product-shot shot-clear" role="img" aria-label="Talbix Facet ballpen with clear barrel and violet grip, shown diagonally"></div>
      <h3 class="product-name">Talbix Facet</h3>
      <p class="product-spec">Tip size: 0.7mm<br>5pcs pouch</p>
      <div class="swatches"><span class="sw-blue"></span><span class="sw-black"></span><span class="sw-red"></span></div>
    </article>
    <article class="product" style="left:444px">
      <div class="product-shot shot-sky" role="img" aria-label="Talbix Glide retractable ballpen in light blue, shown diagonally"></div>
      <h3 class="product-name">Talbix Glide</h3>
      <p class="product-spec">Tip size: 0.7mm<br>5pcs pouch</p>
      <div class="swatches"><span class="sw-blue"></span><span class="sw-black"></span></div>
    </article>
    <div class="carousel-arrows">
      <svg width="30" height="30" viewBox="0 0 30 30"><circle cx="15" cy="15" r="14.5" fill="none" stroke="var(--brand)"/><path d="M18 7 L12 15 L18 23" fill="none" stroke="var(--brand)"/></svg>
      <svg width="30" height="30" viewBox="0 0 30 30"><circle cx="15" cy="15" r="14.5" fill="none" stroke="var(--brand)"/><path d="M12 7 L18 15 L12 23" fill="none" stroke="var(--brand)"/></svg>
    </div>
  </section>

  <footer>
    <div class="footer-band"></div>
    <svg class="wave" style="top:1046px" width="678" height="12" viewBox="0 0 678 12">
      <path d="M0 4 C160 8 320 2 480 6 S620 4 678 5 L678 12 L0 12 Z" fill="var(--footer-band)"/>
      <path d="M0 2 C160 6 320 0 480 4 S620 2 678 3" fill="none" stroke="var(--footer-band)" stroke-width="0.8"/>
    </svg>
    <ul class="contact-list">
      <li><svg width="10" height="12" viewBox="0 0 10 12"><path d="M5 0.5a4 4 0 0 0-4 4c0 3 4 7 4 7s4-4 4-7a4 4 0 0 0-4-4z" fill="none" stroke="var(--white)" stroke-width="1.3"/><circle cx="5" cy="4.5" r="1.3" fill="var(--white)"/></svg>100, Office, City, Country</li>
      <li class="strong"><svg width="11" height="11" viewBox="0 0 11 11"><path d="M2 0.5 L4 3 L3 4.5 C4 6.5 4.5 7 6.5 8 L8 7 L10.5 9 L9 10.7 C4.5 10.5 0.5 6.5 0.3 2 Z" fill="var(--white)"/></svg>123 456 7890</li>
      <li><svg width="12" height="9" viewBox="0 0 12 9"><rect x="0.6" y="0.6" width="10.8" height="7.8" fill="none" stroke="var(--white)" stroke-width="1.1"/><path d="M0.6 0.6 L6 5 L11.4 0.6" fill="none" stroke="var(--white)" stroke-width="1.1"/></svg>info@talbix-example.com</li>
    </ul>
    <div class="social-links" aria-label="Social profiles"><span></span><span></span><span></span></div>
    <div class="legal-bar">© <strong>TALBIX</strong> - 2016. All Rights Reserved.</div>
  </footer>
</body>
</html>
```